Brand new letterhead, business card, email signature etc.

We are a financial company in London, UK. Our website is www.quorvane.com. We're wanting a complete remodel of the company colours, letter head, business cards, email signatures, etc. Looking to keep the same font for the company name. I have upload a colour palette that we want to work with. We're looking for company letterhead for outgoing letters/ correspondence, letterhead for internal documentation, email signatures, e-letters. etc. Ultimately we will redesign the entire website also. It is important that our clients get a strong, secure, warm, trustworthy, solid feeling and first impression.
Updates

Designs look the same

Target Market(s)

Institutional investors, (ultra) high net worth individuals

Industry/Entity Type

Finance, Invesments banking.

Font styles to use
Other font styles liked:
• Current font is "Champagne & Limousines"

Requirements
Must have
• Must use the colours provided on the PDF uploaded to the portal. The purple = main colour. The red = accent colour.
Nice to have
• Nice to use same font as now for the company name "Marlowin". Font is "Champagne & Limousines". Nice to have some reference to the old logo flower, but only subtle.
Should not have
• Do not use the colour red from our website. Use the colours provided on the colour palette PDF that I uploaded in the portal.

```html
<!DOCTYPE html>
<html lang="en">
<head>
<meta charset="utf-8">
<title>Marlowin Stationery</title>
<link href="https://fonts.googleapis.com/css2?family=Josefin+Sans:wght@300&family=Open+Sans:wght@400;700&family=Montserrat:wght@400;500&display=swap" rel="stylesheet">
<style>
  :root{
    --backdrop:#c4c4c4;
    --paper:#ffffff;
    --primary:#4a2762;
    --accent:#be1a32;
    --ink:#2b2b2b;
    --muted:#8a8a8a;
    --body:#8c8c8c;
  }
  *{margin:0;padding:0;box-sizing:border-box}
  html,body{width:1200px;height:825px;overflow:hidden;background:var(--backdrop)}
  body{position:relative;font-family:"Open Sans",Arial,sans-serif;color:var(--ink)}
  .sheet{position:absolute;background:var(--paper);box-shadow:2px 3px 6px rgba(0,0,0,.18);overflow:hidden}
  .abs{position:absolute}
  .brand{position:absolute;display:flex;align-items:center;white-space:nowrap}
  .brand-square{border:1px solid var(--primary);flex:none}
  .brand-name{font-family:"Josefin Sans",sans-serif;font-weight:300;text-transform:uppercase;color:var(--primary);line-height:1}
  .brand--light .brand-square{border-color:#fff}
  .brand--light .brand-name{color:#fff}
  .primary-bar{position:absolute;background:var(--primary)}
  .divider{position:absolute;width:1px;background:var(--accent)}
  .contact{position:absolute;font-family:"Montserrat",sans-serif;color:#222;white-space:nowrap}
  .contact li{list-style:none;display:flex;align-items:center}
  .contact svg{fill:var(--accent);flex:none}
  .address{position:absolute;font-family:"Montserrat",sans-serif;color:#222;white-space:nowrap}

  /* letterhead */
  .letterhead{left:58px;top:72px;width:520px;height:673px}
  .sender-name{left:45px;top:132px;font-size:13px;font-weight:700;color:var(--primary)}
  .sender-details{left:45px;top:153px;font-size:8px;line-height:12.2px;color:var(--muted)}
  .letter-date{right:47px;top:189px;font-size:8px;color:var(--muted)}
  .letter-body{left:45px;top:225px;width:429px;font-size:7.9px;line-height:10.3px;color:var(--body);text-align:justify}
  .letter-body p{margin-bottom:10.3px}
  .signature{left:45px;top:492px;width:105px;height:20px;background:linear-gradient(90deg,#ececec,#f7f7f7)}
  .signer-name{left:45px;top:516px;font-size:11px;font-weight:700;color:var(--primary)}
  .signer-role{left:45px;top:532px;font-size:8px;color:var(--muted)}

  /* envelopes */
  .envelope-front{left:608px;top:75px;width:530px;height:265px}
  .envelope-back{left:608px;top:354px;width:530px;height:264px}
  .envelope-flap{position:absolute;left:0;top:0}

  /* business cards */
  .card-front{left:606px;top:630px;width:215px;height:122px}
  .card-back{left:840px;top:629px;width:214px;height:122px;background:var(--primary)}
  .card-holder{right:124px;top:73px;text-align:right;font-family:"Montserrat",sans-serif;font-size:6px;line-height:8px;color:#222;white-space:nowrap}
  .card-holder .holder-name{font-weight:500;color:var(--primary)}
  .card-holder .role{color:var(--accent)}
  .card-holder .addr{margin-top:4px;line-height:9.5px}
</style>
</head>
<body>

<svg width="0" height="0" style="position:absolute" aria-hidden="true">
  <defs>
    <symbol id="icon-phone" viewBox="0 0 10 10"><path d="M2 0.8l1.6 1.9-0.9 1.1c0.6 1.3 1.4 2.1 2.6 2.6l1.1-0.9 1.9 1.6-1.1 1.6C4.3 8.5 1.5 5.7 0.6 1.9z"/></symbol>
    <symbol id="icon-mobile" viewBox="0 0 10 10"><path d="M2.8 0.5h4.4v9H2.8z M3.6 1.5v6.2h2.8V1.5z" fill-rule="evenodd"/></symbol>
    <symbol id="icon-mail" viewBox="0 0 10 10"><path d="M0.5 2h9v6h-9z M1 2.4l4 3 4-3v-0.1H1z" fill-rule="evenodd"/></symbol>
    <symbol id="icon-globe" viewBox="0 0 10 10"><circle cx="5" cy="5" r="4.5"/><path d="M0.8 5h8.4M5 0.7c-2 2.6-2 6 0 8.6M5 0.7c2 2.6 2 6 0 8.6" stroke="#fff" stroke-width="0.7" fill="none"/></symbol>
  </defs>
</svg>

<!-- Letterhead -->
<section class="sheet letterhead">
  <div class="brand" style="left:45px;top:29px">
    <span class="brand-square" style="width:56px;height:56px"></span>
    <span class="brand-name" style="font-size:26px;letter-spacing:2px;margin-left:13px">Marlowin</span>
  </div>
  <div class="abs sender-name">Name Surname</div>
  <div class="abs sender-details">Senior Executive<br>Address goes here. Street, City, Country<br>contact@yourmail.com<br>000-987-654-321</div>
  <div class="abs letter-date">Date, 10 September, 2030</div>
  <div class="abs letter-body">
    <p>Lorem ipsum dolor sit amet, consectetur adipisicing elit, sed do eiusmod tempor incididunt ut labore et dolore magna aliqua. Ut enim ad minim veniam, quis nostrud exercitation ullamco laboris nisi ut aliquip ex ea commodo consequat. Duis aute irure dolor in reprehenderit in voluptate velit esse cillum dolore eu fugiat nulla pariatur. Excepteur sint occaecat cupidatat non proident, sunt in culpa qui officia deserunt mollit anim id est laborum. Sed ut perspiciatis unde omnis iste natus error sit voluptatem accusantium doloremque laudantium, totam rem aperiam, eaque ipsa quae ab illo inventore veritatis et quasi architecto beatae vitae dicta sunt explicabo. Nemo enim ipsam voluptatem quia voluptas sit aspernatur aut odit aut fugit, sed quia consequuntur magni dolores eos qui ratione voluptatem sequi nesciunt. Neque porro voluptatem sequi nesciunt. Nemo enim ipsam voluptatem quia voluptas.</p>
    <p>Lorem ipsum dolor sit amet, consectetur adipisicing elit, sed do eiusmod tempor incididunt ut labore et dolore magna aliqua. Ut enim ad minim veniam, quis nostrud exercitation ullamco laboris nisi ut aliquip ex ea commodo consequat. Duis aute irure dolor in reprehenderit in voluptate velit esse cillum dolore eu fugiat nulla pariatur. Excepteur sint occaecat cupidatat non proident, sunt in culpa qui officia deserunt mollit anim id est laborum. Sed ut perspiciatis unde omnis iste natus error sit voluptatem accusantium doloremque laudantium, totam rem aperiam, eaque ipsa quae ab illo inventore veritatis et quasi architecto beatae vitae dicta sunt explicabo. Nemo enim ipsam voluptatem quia voluptas sit aspernatur aut odit aut.</p>
    <p>Lorem ipsum dolor sit amet, consectetur adipisicing elit, sed do eiusmod tempor incididunt ut labore et dolore magna aliqua. Ut enim ad minim veniam, quis nostrud exercitation ullamco laboris nisi ut aliquip ex ea commodo consequat. .</p>
  </div>
  <div class="abs signature" role="img" aria-label="Handwritten signature"></div>
  <div class="abs signer-name">NAME SURNAME</div>
  <div class="abs signer-role">General Manager</div>

  <div class="address" style="left:51px;top:632px;font-size:8.6px;line-height:12px">41 Halden Row<br>London, EC2V 7QP</div>
  <div class="divider" style="left:163px;top:612px;height:53px"></div>
  <ul class="contact" style="left:174px;top:619px;font-size:8.6px;line-height:12px">
    <li><svg width="8" height="8"><use href="#icon-phone"/></svg><span style="margin-left:5px">020-7946-0182</span></li>
    <li><svg width="8" height="8"><use href="#icon-mail"/></svg><span style="margin-left:5px">info@yourdomainhere.com</span></li>
    <li><svg width="8" height="8"><use href="#icon-globe"/></svg><span style="margin-left:5px">www.quorvane.com</span></li>
  </ul>
  <div class="primary-bar" style="left:48px;top:667px;width:243px;height:6px"></div>
</section>

<!-- Envelope front -->
<section class="sheet envelope-front">
  <div class="brand" style="left:33px;top:31px">
    <span class="brand-square" style="width:43px;height:43px"></span>
    <span class="brand-name" style="font-size:19px;letter-spacing:2px;margin-left:9px">Marlowin</span>
  </div>
  <div class="address" style="left:33px;top:228px;font-size:8.6px;line-height:12px">41 Halden Row<br>London, EC2V 7QP</div>
  <div class="divider" style="left:145px;top:216px;height:40px"></div>
  <ul class="contact" style="left:156px;top:214px;font-size:8.6px;line-height:12px">
    <li><svg width="8" height="8"><use href="#icon-phone"/></svg><span style="margin-left:5px">020-7946-0182</span></li>
    <li><svg width="8" height="8"><use href="#icon-mail"/></svg><span style="margin-left:5px">info@yourdomainhere.com</span></li>
    <li><svg width="8" height="8"><use href="#icon-globe"/></svg><span style="margin-left:5px">www.quorvane.com</span></li>
  </ul>
  <div class="primary-bar" style="left:30px;top:259px;width:243px;height:6px"></div>
</section>

<!-- Envelope back -->
<section class="sheet envelope-back">
  <svg class="envelope-flap" width="530" height="100" aria-hidden="true">
    <path d="M14 0 C18 40 25 80 55 84 L475 84 C505 80 512 40 516 0" fill="#fff" stroke="#d4d4d4" stroke-width="1.2"/>
  </svg>
  <div class="brand" style="left:203px;top:26px">
    <span class="brand-square" style="width:32px;height:32px"></span>
    <span class="brand-name" style="font-size:15px;letter-spacing:1.8px;margin-left:7px">Marlowin</span>
  </div>
</section>

<!-- Business card front -->
<section class="sheet card-front">
  <div class="brand" style="left:53px;top:14px">
    <span class="brand-square" style="width:27px;height:27px"></span>
    <span class="brand-name" style="font-size:12px;letter-spacing:1.6px;margin-left:8px">Marlowin</span>
  </div>
  <div class="abs card-holder">
    <div class="holder-name">ELENA VARRICK</div>
    <div class="role">Manager</div>
    <div class="addr">41 Halden Row<br>London, EC2V 7QP</div>
  </div>
  <div class="divider" style="left:102px;top:72px;height:36px"></div>
  <ul class="contact" style="left:112px;top:72px;font-size:5.6px;line-height:9.2px">
    <li><svg width="6" height="6"><use href="#icon-phone"/></svg><span style="margin-left:4px">020-7946-0182</span></li>
    <li><svg width="6" height="6"><use href="#icon-mobile"/></svg><span style="margin-left:4px">020-7946-0375</span></li>
    <li><svg width="6" height="6"><use href="#icon-mail"/></svg><span style="margin-left:4px">info@quorvane.com</span></li>
    <li><svg width="6" height="6"><use href="#icon-globe"/></svg><span style="margin-left:4px">www.quorvane.com</span></li>
  </ul>
  <div class="primary-bar" style="left:13px;top:118px;width:178px;height:4px"></div>
</section>

<!-- Business card back -->
<section class="sheet card-back">
  <div class="brand brand--light" style="left:29px;top:40px">
    <span class="brand-square" style="width:40px;height:40px"></span>
    <span class="brand-name" style="font-size:17px;letter-spacing:2px;margin-left:8px">Marlowin</span>
  </div>
</section>

</body>
</html>
```